ambitious event and festival agency from austria needs fresh business card design

A new design is due for the new headquarters and the new challenges. We organize events for different target groups from 16 to 60 years. The design should therefore be straightforward and not confused, so we are open to new colors and the logo may also be changed. In general, however, the most interesting suggestions are the most interesting ones. after this order we are looking for more graphics for partyvelt facebook instagramm homepage etc A new design is due for the new headquarters and the new challenges. We organize events for different target groups from 16 to 60 years. The design should therefore be straightforward and not confused, so we are open to new colors and the logo may also be changed. In general, however, the most interesting suggestions are the most interesting ones. after this order we are looking for more graphics for partyvelt facebook instagramm homepage etc A new design is due for the new headquarters and the new challenges. We organize events for different target groups from 16 to 60 years. The design should therefore be straightforward and not confused, so we are open to new colors and the logo may also be changed. In general, however, the most interesting suggestions are the most interesting ones. after this order we are looking for more graphics for partyvelt facebook instagramm homepage etc

Reason: I am sorry for this decision but i need some more time. No new designs please, there are so many good ones and I will have made a decision in the next 3 days.

Target Market(s)

Industry/Entity Type

Business

Font styles to use
Serif
Sans Serif

Colors

Designer to choose colors to be used in the design.

Requirements
Must have
Nice to have
Should not have

```html
<!DOCTYPE html>
<html lang="de">
<head>
<meta charset="utf-8">
<title>partyvelt – Visitenkarte</title>
<link rel="stylesheet" href="https://fonts.googleapis.com/css2?family=Lato:wght@400;700;900&display=swap">
<style>
  :root {
    --page: #ecebe8;
    --paper: #f7f7f6;
    --red: #cc2e48;
    --red-deep: #b5233c;
    --grey: #7a8286;
    --logo-grey: #8a9296;
    --white: #ffffff;
  }
  * { box-sizing: border-box; margin: 0; padding: 0; }
  html, body { width: 1200px; height: 780px; overflow: hidden; }
  body {
    background: var(--page);
    font-family: "Lato", Arial, sans-serif;
    display: flex;
    align-items: center;
    justify-content: center;
    gap: 40px;
  }
  .card {
    width: 540px;
    height: 310px;
    border-radius: 3px;
    overflow: hidden;
    box-shadow: 0 6px 18px rgba(0,0,0,0.18);
    position: relative;
  }

  /* front */
  .card-front { display: flex; flex-direction: column; background: var(--paper); }
  .front-brand {
    height: 122px;
    display: flex;
    align-items: center;
    justify-content: center;
  }
  .wordmark {
    font-weight: 900;
    letter-spacing: -1px;
    line-height: 1;
  }
  .front-brand .wordmark { font-size: 62px; color: var(--red); }
  .front-details {
    flex: 1;
    background: linear-gradient(180deg, var(--red) 0%, var(--red-deep) 100%);
    display: flex;
    align-items: center;
    padding: 0 34px;
    color: var(--white);
  }
  .person { flex: 1; text-align: right; padding-right: 26px; }
  .person-name { font-size: 22px; font-weight: 700; }
  .person-role { font-size: 15px; margin-top: 4px; }
  .divider { width: 1px; height: 82px; background: rgba(255,255,255,0.8); }
  .contacts { flex: 1.3; list-style: none; padding-left: 24px; }
  .contacts li {
    display: flex; align-items: center; gap: 10px;
    font-size: 14px; line-height: 26px;
  }
  .contacts svg { width: 18px; height: 18px; flex: none; }
  .front-address {
    height: 38px;
    background: var(--grey);
    color: var(--white);
    display: flex; align-items: center; justify-content: center;
    font-size: 14px;
    letter-spacing: 0.3px;
  }

  /* back */
  .card-back {
    background: linear-gradient(160deg, #d8344f 0%, var(--red) 50%, var(--red-deep) 100%);
    display: flex;
    flex-direction: column;
    justify-content: center;
    padding-left: 70px;
  }
  .card-back .wordmark { font-size: 68px; color: var(--white); }
  .back-web { color: var(--white); font-size: 15px; letter-spacing: 1px; margin-top: 16px; padding-left: 4px; }
</style>
</head>
<body>
  <section class="card card-front" aria-label="Visitenkarte Vorderseite">
    <div class="front-brand"><span class="wordmark">partyvelt</span></div>
    <div class="front-details">
      <div class="person">
        <p class="person-name">Markus Feldhofer</p>
        <p class="person-role">Geschäftsführer</p>
      </div>
      <div class="divider"></div>
      <ul class="contacts">
        <li>
          <svg viewBox="0 0 18 18" aria-hidden="true"><circle cx="9" cy="9" r="8.2" fill="none" stroke="#fff" stroke-width="1.2"/><rect x="6.3" y="4.3" width="5.4" height="9.4" rx="1" fill="none" stroke="#fff" stroke-width="1.2"/></svg>
          +43 660 482 317 5
        </li>
        <li>
          <svg viewBox="0 0 18 18" aria-hidden="true"><circle cx="9" cy="9" r="8.2" fill="none" stroke="#fff" stroke-width="1.2"/><rect x="4.5" y="6" width="9" height="6.2" fill="none" stroke="#fff" stroke-width="1.2"/><path d="M4.5 6 L9 9.6 L13.5 6" fill="none" stroke="#fff" stroke-width="1.2"/></svg>
          m.feldhofer@partyvelt.eu
        </li>
        <li>
          <svg viewBox="0 0 18 18" aria-hidden="true"><circle cx="9" cy="9" r="8.2" fill="none" stroke="#fff" stroke-width="1.2"/><circle cx="9" cy="9" r="4.8" fill="none" stroke="#fff" stroke-width="1"/><ellipse cx="9" cy="9" rx="2" ry="4.8" fill="none" stroke="#fff" stroke-width="1"/><line x1="4.2" y1="9" x2="13.8" y2="9" stroke="#fff" stroke-width="1"/></svg>
          www.partyvelt.eu
        </li>
      </ul>
    </div>
    <div class="front-address">partyvelt Birkenau 12, A4520 Talfeld</div>
  </section>

  <section class="card card-back" aria-label="Visitenkarte Rückseite">
    <span class="wordmark">partyvelt</span>
    <p class="back-web">www.partyvelt.eu</p>
  </section>
</body>
</html>
```